TRENDY & MODERN BUSINESS CARD DESIGN for Media Company *

I need a minimalistic - clean - modern and professional business card layout and design for MEDIA & PHOTOGRAPHY STUDIO.

We do NOT have a logo, and not really looking for one - but rather excellent typography and design. We would consider the 3 as a focal point.

We do personal and commercial photography.

Target Market(s)

Personal and commercial photography clientele

Contact Information for Business Card

ZUB size - from zub.com / size guidelines are enclosed in the brief

Font styles to use
Sans Serif

Colors
f78f20
eda3c7
cee9f5
0555a3
e667a6
fbf289

Requirements
Must have
• Clean lines - Modern layout
Nice to have
• All blue background as an option - use color palette in brief please.
Should not have
• Old fashion fonts and regular fonts.

```html
<!DOCTYPE html>
<html lang="en">
<head>
<meta charset="utf-8">
<title>Brightfield Studio – Business Card</title>
<link rel="stylesheet" href="https://fonts.googleapis.com/css2?family=Open+Sans:wght@400;600;700&family=Roboto+Condensed:wght@400&display=swap">
<style>
  :root {
    --stage: #2b2b2d;
    --card: #1f1f21;
    --card-back: #222224;
    --text-main: #e6e6e6;
    --text-soft: #c4c4c4;
    --rule: #5a5a5c;
    --pink: #e667a6;
    --yellow: #fbf289;
  }
  * { box-sizing: border-box; margin: 0; padding: 0; }
  html, body {
    width: 1200px; height: 1108px; overflow: hidden;
    background: var(--stage);
  }
  .stage {
    position: relative; width: 1200px; height: 1108px;
    display: flex; justify-content: center; align-items: center; gap: 60px;
  }
  .card {
    position: relative; width: 440px; height: 720px;
    border-radius: 26px; background: var(--card);
    box-shadow: 0 18px 40px rgba(0,0,0,.45);
    overflow: hidden;
  }
  /* Front */
  .card--front { display: flex; flex-direction: column; align-items: center; }
  .brand-mark {
    margin-top: 130px; display: flex; align-items: center; gap: 14px;
    font-family: "Open Sans", sans-serif; font-weight: 700;
    font-size: 30px; color: var(--yellow); letter-spacing: .5px;
  }
  .brand-mark__dot { width: 26px; height: 26px; border-radius: 50%; background: var(--pink); }
  .contact {
    margin-top: 150px; width: 300px; text-align: center;
    font-family: "Open Sans", sans-serif; color: var(--text-soft);
  }
  .contact__name { font-weight: 700; font-size: 23px; color: var(--text-main); letter-spacing: .3px; text-transform: uppercase; }
  .contact__role { font-size: 18px; margin-top: 2px; }
  .contact__rule { height: 1px; background: var(--rule); margin: 12px 10px; }
  .contact__line { font-size: 18px; line-height: 1.35; }
  /* Back */
  .card--back { background: var(--card-back); }
  .back-texture {
    position: absolute; inset: 0 0 200px 0;
    background: linear-gradient(180deg, #262628 0%, #222224 100%);
  }
  .back-brand {
    position: absolute; left: 0; right: 0; bottom: 96px; text-align: center;
  }
  .back-brand__dot {
    width: 120px; height: 120px; border-radius: 50%; background: var(--pink);
    margin: 0 auto 26px;
  }
  .back-brand__name {
    font-family: "Roboto Condensed", sans-serif; font-size: 40px; color: var(--text-main);
    letter-spacing: .5px; text-transform: uppercase;
  }
  .back-brand__tagline {
    margin-top: 4px; font-family: "Open Sans", sans-serif; font-size: 13px;
    letter-spacing: 4px; color: var(--text-soft); text-transform: uppercase;
  }
</style>
</head>
<body>
<main class="stage">
  <section class="card card--front" aria-label="Card front">
    <div class="brand-mark"><span class="brand-mark__dot"></span>Brightfield Studio</div>
    <div class="contact">
      <p class="contact__name">Marisol Vega</p>
      <p class="contact__role">Founder &amp; Media Director</p>
      <div class="contact__rule"></div>
      <p class="contact__line">(305) 555-0142</p>
      <p class="contact__line">mv@brightfieldstudio.com</p>
      <div class="contact__rule"></div>
      <p class="contact__line">2400 Coral Way</p>
      <p class="contact__line">4th Floor, Miami, FL 33145</p>
      <div class="contact__rule"></div>
      <p class="contact__line">Tampa • Boston</p>
      <p class="contact__line">Denver • Lima • Oslo</p>
    </div>
  </section>

  <section class="card card--back" aria-label="Card back">
    <div class="back-texture" role="img" aria-label="Faint repeating studio pattern on dark background"></div>
    <div class="back-brand">
      <div class="back-brand__dot"></div>
      <p class="back-brand__name">Brightfield Studio</p>
      <p class="back-brand__tagline">Every moment, framed well</p>
    </div>
  </section>
</main>
</body>
</html>
```